Before the kettle cools, pocast with content in its majority of technology

Page dedicated to a pocast with content in its majority of technology. The page also contains the chapters of the podcast (pluggin tunebrim) will also contain news. Preferably Worpress. There is already a very basic page with a simple theme, the logo and little more, I would like something more professional. Www.cuandoelfarosebalancea.com The logo does not want to change.

Target Market(s)

Anyone

Colors

Requirements
Must have
• You can put the tunebrim pluggin with the podcast chapters

```html
<!DOCTYPE html>
<html lang="es">
<head>
<meta charset="utf-8">
<title>Before the kettle cools — podcast</title>
<link href="https://fonts.googleapis.com/css2?family=Roboto:wght@400;500;700&display=swap" rel="stylesheet">
<style>
:root{
  --orange:#f07d1a;
  --orange-light:#f7a233;
  --text:#555;
  --title:#222;
  --muted:#999;
  --line:#e6e6e6;
  --panel:#f2f2f2;
  --yellow:#f5b800;
  --teal:#1aa38f;
  --green:#2bb37a;
  --blue:#3a7bd5;
  --wave:#cfcfcf;
}
*{box-sizing:border-box;margin:0;padding:0}
html,body{width:1200px;height:3930px;overflow:hidden}
body{font-family:"Roboto",Arial,sans-serif;color:var(--text);background:#fff;position:relative;font-size:12px;line-height:20px}
.site-header{position:absolute;left:0;top:0;width:1200px;height:136px;background:linear-gradient(90deg,#101010,#2c2c2c 45%,#3a3a3a 80%,#1a1a1a)}
.brand{position:absolute;left:152px;top:40px;display:flex;align-items:center;gap:12px}
.brand-dot{width:44px;height:44px;border-radius:50%;background:var(--orange)}
.brand-name{color:var(--orange);font-weight:700;font-size:18px;line-height:22px;width:170px}
.header-social{position:absolute;left:960px;top:20px;display:flex;gap:8px}
.header-social span{width:34px;height:34px;border-radius:50%;border:2px solid #fff}
.header-actions{position:absolute;left:890px;top:84px;display:flex;gap:14px}
.btn{height:32px;padding:0 18px;font-size:11px;font-weight:700;line-height:32px;color:#fff;letter-spacing:.5px}
.btn-register{border:1px solid #fff;line-height:30px}
.btn-login{background:var(--orange)}
.post{position:absolute;left:110px;width:650px}
.post-title{font-size:19px;line-height:26px;font-weight:500;color:var(--title)}
.post-meta{margin-top:6px;font-size:11px;color:var(--muted);display:flex;gap:18px;align-items:center}
.post-meta .author{color:var(--orange)}
.meta-ico{display:inline-block;width:10px;height:10px;background:#aaa;border-radius:2px;margin-right:5px;vertical-align:-1px}
.post-body p{margin-top:14px}
.share{display:flex;align-items:center;justify-content:space-between;border-bottom:1px solid var(--line);padding:10px 0;margin-top:18px}
.share-left{display:flex;align-items:center;gap:5px}
.share-label{font-size:10px;font-weight:700;color:var(--title);margin-right:6px}
.share-left i{width:20px;height:20px;border-radius:50%;display:block}
.share-right{font-size:10px;color:var(--muted)}
.pricing{margin-top:26px;border:1px solid #ddd;padding:10px 16px;display:flex;gap:20px;background:#fafafa}
.plan{flex:1;background:#fff;border:1px solid #ddd;text-align:center;padding-bottom:10px}
.plan-top{display:flex;justify-content:space-between;padding:6px 10px;font-size:10px;color:#aaa}
.plan-top b{color:var(--teal);font-size:18px}
.plan-price{font-size:22px;color:#333;margin:22px 0 6px}
.plan-price small{font-size:10px;color:var(--teal)}
.plan-old{font-size:10px;color:#aaa;text-decoration:line-through;height:14px}
.plan-bar{background:var(--green);color:#fff;font-size:9px;margin-top:12px;height:18px;line-height:18px}
.plan-radio{width:12px;height:12px;border:1px solid #aaa;border-radius:50%;margin:8px auto 0}
.plan-radio.on{background:var(--blue);border-color:var(--blue)}
.player{margin-top:26px;height:208px;display:flex;border:1px solid var(--line)}
.player-main{flex:1;position:relative;background:#fff}
.player.dark .player-main{background:#111}
.play{position:absolute;left:12px;top:14px;width:76px;height:76px;border-radius:50%;background:var(--yellow)}
.play svg{position:absolute;left:28px;top:22px}
.ep-title{position:absolute;left:100px;top:16px;width:200px;font-size:16px;line-height:22px;color:#333}
.player.dark .ep-title{color:#fff}
.host{position:absolute;right:12px;top:14px;font-size:12px;font-weight:700;color:#333}
.player.dark .host{color:#fff}
.ep-actions{position:absolute;left:100px;top:74px;font-size:11px;color:#333;display:flex;gap:18px}
.player.dark .ep-actions{color:#fff}
.times{position:absolute;left:12px;right:12px;top:108px;display:flex;justify-content:space-between;font-size:10px;color:#888}
.wave{position:absolute;left:0;bottom:0;color:var(--wave)}
.player.dark .wave{color:#777}
.player-art{width:210px}
.pagination{position:absolute;left:110px;top:3666px;width:650px;display:flex;justify-content:center;gap:8px}
.pagination span{height:30px;min-width:30px;padding:0 10px;border:1px solid #ccc;border-radius:15px;font-size:10px;line-height:28px;text-align:center;color:#888}
.pagination .current{border-color:var(--orange);color:var(--orange)}
.sidebar{position:absolute;left:828px;top:194px;width:257px}
.search{background:var(--panel);padding:18px}
.search div{background:#fff;border:1px solid #ddd;height:38px;font-size:11px;color:#aaa;padding:0 10px;line-height:36px}
.widget{margin-top:28px;border:3px solid var(--orange);background:#fff}
.widget h3{background:var(--orange);color:#fff;font-size:15px;font-weight:500;padding:10px 16px}
.widget ul{list-style:none;padding:4px 16px 10px}
.widget li{font-size:11.5px;line-height:17px;color:#444;border-bottom:1px solid var(--line);padding:10px 0}
.widget li:last-child{border-bottom:none}
.widget.contact{border-color:var(--orange-light)}
.widget.contact h3{background:var(--orange-light)}
.widget.contact li{border:none;padding:7px 0;display:flex;align-items:center;gap:10px;color:#666}
.widget.contact li i{width:9px;height:9px;border-radius:50%;background:#999}
.site-footer{position:absolute;left:0;top:3700px;width:1200px;height:230px;background:#eeeeee;text-align:center}
.footer-social{display:flex;justify-content:center;gap:10px;margin-top:40px}
.footer-social span{width:36px;height:36px;border-radius:50%}
.site-footer p{font-size:11px;color:#888;line-height:18px}
.site-footer p:first-of-type{margin-top:16px}
</style>
</head>
<body>

<svg width="0" height="0" style="position:absolute">
  <defs>
    <symbol id="wave-bars" viewBox="0 0 433 70">
      <path fill="currentColor" d="M0 70V40h3v30zM6 70V30h3v40zM12 70V48h3v22zM18 70V22h3v48zM24 70V38h3v32zM30 70V50h3v20zM36 70V28h3v42zM42 70V44h3v26zM48 70V34h3v36zM54 70V52h3v18zM60 70V26h3v44zM66 70V40h3v30zM72 70V46h3v24zM78 70V32h3v38zM84 70V50h3v20zM90 70V36h3v34zM96 70V24h3v46zM102 70V44h3v26zM108 70V52h3v18zM114 70V30h3v40zM120 70V40h3v30zM126 70V48h3v22zM132 70V34h3v36zM138 70V26h3v44zM144 70V46h3v24zM150 70V38h3v32zM156 70V52h3v18zM162 70V30h3v40zM168 70V42h3v28zM174 70V22h3v48zM180 70V44h3v26zM186 70V36h3v34zM192 70V50h3v20zM198 70V28h3v42zM204 70V40h3v30zM210 70V48h3v22zM216 70V32h3v38zM222 70V44h3v26zM228 70V26h3v44zM234 70V38h3v32zM240 70V52h3v18zM246 70V34h3v36zM252 70V46h3v24zM258 70V28h3v42zM264 70V42h3v28zM270 70V50h3v20zM276 70V24h3v46zM282 70V40h3v30zM288 70V46h3v24zM294 70V32h3v38zM300 70V52h3v18zM306 70V36h3v34zM312 70V28h3v42zM318 70V44h3v26zM324 70V40h3v30zM330 70V50h3v20zM336 70V30h3v40zM342 70V42h3v28zM348 70V24h3v46zM354 70V46h3v24zM360 70V36h3v34zM366 70V52h3v18zM372 70V32h3v38zM378 70V44h3v26zM384 70V26h3v44zM390 70V40h3v30zM396 70V48h3v22zM402 70V34h3v36zM408 70V50h3v20zM414 70V30h3v40zM420 70V42h3v28zM426 70V38h3v32z"/>
    </symbol>
    <symbol id="play-arrow" viewBox="0 0 26 32"><path d="M0 0L26 16L0 32Z" fill="#fff"/></symbol>
  </defs>
</svg>

<header class="site-header" role="img" aria-label="Cabecera oscura con fotografía de un micrófono de estudio">
  <div class="brand"><span class="brand-dot"></span><span class="brand-name">Before the kettle cools</span></div>
  <div class="header-social"><span></span><span></span><span></span></div>
  <div class="header-actions"><span class="btn btn-register">REGISTER</span><span class="btn btn-login">LOGIN</span></div>
</header>

<article class="post" style="top:186px">
  <h2 class="post-title">Cambio de logo</h2>
  <div class="post-meta"><span class="author"><i class="meta-ico"></i>De Naviro</span><span><i class="meta-ico"></i>19 May, 2017</span><span><i class="meta-ico"></i>20 Comments</span></div>
  <div class="post-body">
    <p>Hola a Tod@s!</p>
    <p>¿Salta a la vista no?, pues sí, renovamos diseño del logo y algo en la web. Aquí los cambios irán poco a poco pero procuraré dejar todo lo que quiero modificar hecho en una semana (como mucho, todo dependerá del tiempo que le pueda dedicar aunque lo difícil ya está hecho.</p>
    <p>Nada más, nos escuchamos en el siguiente</p>
  </div>
  <div class="share" style="margin-top:30px">
    <div class="share-left"><span class="share-label">COMPARTE:</span><i style="background:#4aa3df"></i><i style="background:#3b5b98"></i><i style="background:#d44"></i><i style="background:#ccc"></i><i style="background:#2a6fb0"></i><i style="background:#2bb37a"></i><i style="background:#c0392b"></i><i style="background:#888"></i><i style="background:#888"></i></div>
    <div class="share-right">Publicado en Sin categoría | Deja un comentario</div>
  </div>
</article>

<article class="post" style="top:512px">
  <h2 class="post-title">¿Te gustan las series?¿Conoces serievista.tv?</h2>
  <div class="post-meta"><span class="author"><i class="meta-ico"></i>De Naviro</span><span><i class="meta-ico"></i>17 May, 2017</span><span><i class="meta-ico"></i>20 Comments</span></div>
  <div class="post-body">
    <p>Hola a todo@s!</p>
    <p>Hoy capítulo dedicado a los amantes de las series y las películas. Se trata del servicio de vídeo en streaming de la web serievista.tv portal dedicado al aprendizaje de inglés mediante el método de ver películas y series en inglés con subtítulos.</p>
    <p>El catálogo es muy amplio, actual y completo. Están prácticamente todas las series de la actualidad al día y los clásicos más famosos. Te puedes registrar desde una cuenta de redes sociales, rápido y sencillo. Hay opciones gratuitas (límite de 60 minutos al día) y de pago, donde se elimina el límite de minutos y permite descargas. Estos son los precios:</p>
    <div class="pricing">
      <div class="plan"><div class="plan-top"><b>1</b><span>mes</span></div><div class="plan-price">6<small>€</small></div><div class="plan-old"></div><div class="plan-bar">base</div><div class="plan-radio"></div></div>
      <div class="plan"><div class="plan-top"><b>3</b><span>meses</span></div><div class="plan-price">16<small>€</small></div><div class="plan-old">18 €</div><div class="plan-bar">descuento de 11%</div><div class="plan-radio on"></div></div>
      <div class="plan"><div class="plan-top"><b>6</b><span>meses</span></div><div class="plan-price">28<small>€</small></div><div class="plan-old">36 €</div><div class="plan-bar">descuento de 22%</div><div class="plan-radio"></div></div>
      <div class="plan"><div class="plan-top"><b>12</b><span>meses</span></div><div class="plan-price">48<small>€</small></div><div class="plan-old">72 €</div><div class="plan-bar">descuento de 33%</div><div class="plan-radio"></div></div>
    </div>
    <p style="margin-top:20px">Es fácil conseguir descuentos sobre todo en la cuenta anual, actualmente están ofreciendo 2 años por 48€ en lugar de un año. Buscadlo un poco y veréis.</p>
    <p>En el catálogo entran todas las plataformas actuales, hay series de Cinevra, CasaTV, Vastmart series, etc. En una búsqueda rápida no echaréis de menos ninguna serie.</p>
    <p>Por ponerle una pega, no tiene aplicación de dispositivo móvil aunque no le haga falta, es html5 y desde cualquier navegador de un dispositivo móvil funciona muy bien y se puede poner a pantalla completa.</p>
    <p>Es gratis probadlo y veréis.</p>
    <p>Nos escuchamos en el siguiente.</p>
  </div>
  <div class="player">
    <div class="player-main">
      <div class="play"><svg width="26" height="32"><use href="#play-arrow"/></svg></div>
      <div class="ep-title">¿Te gustan las series?¿Conoces serievista.tv?</div>
      <div class="host">tunebrim</div>
      <div class="ep-actions"><span>♥ 1</span><span>● 0</span><span>◁</span></div>
      <div class="times"><span>00:00</span><span>10:58</span></div>
      <svg class="wave" width="433" height="70"><use href="#wave-bars"/></svg>
    </div>
    <div class="player-art" role="img" aria-label="Collage de carteles de series" style="background:linear-gradient(135deg,#3b3025,#1e1b1a 50%,#5a4632)"></div>
  </div>
  <div class="share">
    <div class="share-left"><span class="share-label">COMPARTE:</span><i style="background:#4aa3df"></i><i style="background:#3b5b98"></i><i style="background:#d44"></i><i style="background:#ccc"></i><i style="background:#2a6fb0"></i><i style="background:#2bb37a"></i><i style="background:#c0392b"></i><i style="background:#888"></i><i style="background:#888"></i></div>
    <div class="share-right">Publicado en Sin categoría | Deja un comentario</div>
  </div>
</article>

<article class="post" style="top:1628px">
  <h2 class="post-title">Seguridad en tu Mail</h2>
  <div class="post-meta"><span class="author"><i class="meta-ico"></i>De Naviro</span><span><i class="meta-ico"></i>23 Nov, 2016</span><span><i class="meta-ico"></i>20 Comments</span></div>
  <div class="post-body">
    <p>¡Hola a todos!</p>
    <p>Hoy poco más que decir por aquí de lo dicho en el podcast. Para aquellos que necesiten un punto más de seguridad en el correo electrónico está SelloMail. Planes gratuitos y de pago, codificación, mensajes que se pueden auto destruir, etc.</p>
    <p>SelloMail</p>
  </div>
  <div class="player" style="margin-top:30px">
    <div class="player-main">
      <div class="play"><svg width="26" height="32"><use href="#play-arrow"/></svg></div>
      <div class="ep-title">Seguridad en tu Mail</div>
      <div class="host">tunebrim</div>
      <div class="ep-actions" style="top:50px"><span>♥</span><span>●</span><span>◁</span></div>
      <div class="times"><span>00:00</span><span>09:53</span></div>
      <svg class="wave" width="433" height="70"><use href="#wave-bars"/></svg>
    </div>
    <div class="player-art" role="img" aria-label="Ilustración de un sobre de correo cerrado" style="background:#3b3f85"></div>
  </div>
  <div class="share">
    <div class="share-left"><span class="share-label">COMPARTE:</span><i style="background:#4aa3df"></i><i style="background:#3b5b98"></i><i style="background:#d44"></i><i style="background:#ccc"></i><i style="background:#2a6fb0"></i><i style="background:#2bb37a"></i><i style="background:#c0392b"></i><i style="background:#888"></i><i style="background:#888"></i></div>
    <div class="share-right">Publicado en Sin categoría | Deja un comentario</div>
  </div>
</article>

<article class="post" style="top:2191px">
  <h2 class="post-title">Kaimu KPad2, calidad precio insuperable</h2>
  <div class="post-meta"><span class="author"><i class="meta-ico"></i>De Naviro</span><span><i class="meta-ico"></i>20 Nov, 2016</span><span><i class="meta-ico"></i>20 Comments</span></div>
  <div class="post-body">
    <p>Con un poco de retraso publicamos el post del podcast de la tableta de Kaimu. Tableta que como viene siendo habitual de la marca, da mucho más de lo que cuesta.</p>
    <p>Os lo comento más detalladamente en el podcast pero es una tableta con un chip Corex Q5-R4410, que permite la instalación de Ventana OS además de Droidix. 2 Gb de RAM, almacenamiento de 16 ó 64, 7,9 pulgadas en una fantástica pantalla, que la hacen cumplir más que de sobra en su funcionamiento y a un precio muy apetecible.</p>
    <p>Además como en mi caso, no es raro conseguir un cupón de descuento para poder adquirirla a un mejor precio.</p>
    <p>Si tenéis cualquier duda os lo respondo en los comentarios.</p>
    <p>Un saludo y nos escuchamos en el siguiente</p>
  </div>
  <div class="player" style="margin-top:22px">
    <div class="player-main">
      <div class="play"><svg width="26" height="32"><use href="#play-arrow"/></svg></div>
      <div class="ep-title">Kaimu KPad2, calidad precio insuperable</div>
      <div class="host">tunebrim</div>
      <div class="ep-actions"><span>♥ 2</span><span>● 0</span><span>◁</span></div>
      <div class="times"><span>00:00</span><span>25:31</span></div>
      <svg class="wave" width="433" height="70"><use href="#wave-bars"/></svg>
    </div>
    <div class="player-art" role="img" aria-label="Imagen de marca de la tableta sobre fondo naranja" style="background:#f26b1d"></div>
  </div>
  <div class="share">
    <div class="share-left"><span class="share-label">COMPARTE:</span><i style="background:#4aa3df"></i><i style="background:#3b5b98"></i><i style="background:#d44"></i><i style="background:#ccc"></i><i style="background:#2a6fb0"></i><i style="background:#2bb37a"></i><i style="background:#c0392b"></i><i style="background:#888"></i><i style="background:#888"></i></div>
    <div class="share-right">Publicado en Sin categoría | Deja un comentario</div>
  </div>
</article>

<article class="post" style="top:2888px">
  <h2 class="post-title">Podcast futuros, tunebrim, seriere recomendada</h2>
  <div class="post-meta"><span class="author"><i class="meta-ico"></i>De Naviro</span><span><i class="meta-ico"></i>25 Jul 2016</span><span><i class="meta-ico"></i>20 Comments</span></div>
  <div class="post-body">
    <p>Podcast de hoy variado, un adelanto de uno o una serie (ya veremos) de podcast que voy a grabar en un futuro, opinión de los nuevos planes de precios de tunebrim y la recomendación de una serie Los Restantes.</p>
    <p>Como ya os comento en el podcast el tema Notaria está ya muy adelantado, sólo falta determinar el formato, uno más largo 2 cortos, uno a cada aplicación... Ya veremos.</p>
    <p>Tema tunebrim, hay subida de precios y cambios en las cuentas gratuitas como la mía, menos horas de alojamiento de los podcast, se reducen de la mitad de horas y las cuentas premium aumentan de precio. Yo seguiré igual, cuenta gratuita cuando sea necesario se borraran podcast, el feed tiene de tunebrim y no me apetece de momento estar haciendo cambios. Los podcast también se suben a Voxbay (enlace de Voxbay), así que si necesitáis alguno que se haya borrado de tunebrim, allí los tenéis.</p>
    <p>Los Restantes, primera temporada usuamen buena, de menos a más, pero la segunda es una maravilla, merece ver la serie para ver esa segunda temporada (y que la primera tampoco está mal). Otra recomendación es su banda sonora.</p>
    <p>Y poco más, nos escuchamos en el siguiente.</p>
  </div>
  <div class="player dark" style="margin-top:22px">
    <div class="player-main">
      <div class="play"><svg width="26" height="32"><use href="#play-arrow"/></svg></div>
      <div class="ep-title">Podcast futuros, tunebrim, serie recomendada</div>
      <div class="host">tunebrim</div>
      <div class="ep-actions"><span>♥</span><span>●</span><span>◁</span></div>
      <div class="times"><span>00:00</span><span>13:20</span></div>
      <svg class="wave" width="433" height="70"><use href="#wave-bars"/></svg>
    </div>
    <div class="player-art" role="img" aria-label="Fotografía de una escena submarina en tonos azules" style="background:linear-gradient(160deg,#0d2233,#1f5a78 55%,#0a1a26)"></div>
  </div>
  <div class="share">
    <div class="share-left"><span class="share-label">COMPARTE:</span><i style="background:#4aa3df"></i><i style="background:#3b5b98"></i><i style="background:#d44"></i><i style="background:#ccc"></i><i style="background:#2a6fb0"></i><i style="background:#2bb37a"></i><i style="background:#c0392b"></i><i style="background:#888"></i><i style="background:#888"></i></div>
    <div class="share-right">Publicado en Sin categoría | Deja un comentario</div>
  </div>
</article>

<nav class="pagination"><span>« Prev</span><span class="current">01</span><span>02</span><span>03</span><span>05</span><span>06</span><span>Next »</span></nav>

<aside class="sidebar">
  <div class="search"><div>Buscar...</div></div>
  <section class="widget">
    <h3>Recent Posts</h3>
    <ul>
      <li>Cambio de logo</li>
      <li>¿Te gustan las series?¿Conoces serievista.tv?</li>
      <li>Un anuncio y una prueba</li>
      <li>Seguridad en tu Mail</li>
      <li>Kaimu KPad2, calidad precio insuperable</li>
    </ul>
  </section>
  <section class="widget contact">
    <h3>Contacto</h3>
    <ul>
      <li><i></i>Trinos</li>
      <li><i></i>tunebrim</li>
      <li><i></i>Voxbay</li>
      <li><i></i>Mail</li>
    </ul>
  </section>
</aside>

<footer class="site-footer">
  <div class="footer-social"><span style="background:#3b5b98"></span><span style="background:#4aa3df"></span><span style="background:#d44"></span></div>
  <p>Copyright © 2017 Before the kettle cools. All Rights Reserved.</p>
  <p>Terms of Use | Privacy Policy | Sitemap</p>
</footer>

</body>
</html>
```